Arzt im ästhetischen Bereich sucht seriöses Flyer-Design
Zielgruppe
Ich bin Arzt und nebenberuflich mache ich Eingriffe im ästhetischen Bereich (Lumex- und Hyaluronunterspritzung, Lipolyse, Eigenblutbehandlung (PRP) bzw. Perlglanzkur).
Ich möchte gerne einen sechsseitigen Flyer mit Falz. Auf der Deckseite sollte ein schönes Logo mit ästhetischen Bezug stehen, auf den anderen Seiten werden je die Behandlungsmethoden erklärt (Text kann ich zusteuern bzw. füge ich nach Erhalt des Designs ein). Es sollten auf jeder Seite schöne Abbildungen (entweder Fotomaterial oder auch Zeichnungen) der Methoden enthalten sein. Auf der letzten Seite sollen meine Kontaktdaten stehen
Aufgabenstellung
s.o. 6 seitiger Flyer mit Falzen. Farbe frei. Design medizinisch-ästhetisch mit seriösen Eindruck. Logo von mir soll auf der Rückseite mit meinen Kontaktdaten eingefügt werden.

```html
<!DOCTYPE html>
<html lang="de">
<head>
<meta charset="utf-8">
<title>Flyer Ästhetische Medizin</title>
<link href="https://fonts.googleapis.com/css2?family=Montserrat:wght@400;600;700&family=Oswald:wght@400&display=swap" rel="stylesheet">
<style>
  :root{
    --stage:#d9dadc;
    --paper:#ffffff;
    --sky:#4aaee0;
    --sky-light:#7cc4e6;
    --petrol:#2a4d63;
    --heading:#3a5a75;
    --ink:#2b2b2b;
    --skin:#efd2c2;
    --glove:#8fc9ea;
  }
  *{margin:0;padding:0;box-sizing:border-box}
  html,body{width:1200px;height:676px;overflow:hidden}
  body{background:var(--stage);font-family:"Montserrat",sans-serif;position:relative}
  .flyer{position:absolute;left:150px;top:9px;width:900px;height:636px;background:var(--paper);overflow:hidden;box-shadow:0 6px 14px rgba(0,0,0,.25)}
  .top-band{position:absolute;left:0;top:0;width:900px;height:20px;background:var(--sky)}
  .photo{position:absolute}
  .photo-lips{left:0;top:20px;width:276px;height:368px;background:linear-gradient(180deg,var(--skin) 0%,#e9c6b3 40%,rgba(143,201,234,.55) 75%,var(--paper) 100%)}
  .photo-eye{left:312px;top:20px;width:267px;height:230px;background:linear-gradient(160deg,#e8c6b4 0%,#d8b8a8 45%,#6e9fb5 75%,#a9cfe3 92%,var(--paper) 100%)}
  .photo-face{left:596px;top:20px;width:304px;height:520px;background:linear-gradient(180deg,#f2f2f2 0%,var(--skin) 25%,#ecc9b6 65%,var(--glove) 100%)}
  .section-title{position:absolute;font-weight:600;font-size:16px;line-height:20px;color:var(--heading);text-decoration:underline;text-underline-offset:2px}
  .copy{position:absolute;font-size:10px;line-height:12.8px;color:var(--ink);white-space:nowrap}
  .copy p{margin-bottom:12.8px}
  .title-lumex{left:19px;top:337px}
  .copy-lumex{left:19px;top:372px}
  .title-prp{left:314px;top:273px}
  .copy-prp{left:314px;top:304px}
  .wave{position:absolute;left:0;top:0}
  .badge{position:absolute;left:673px;top:449px;width:150px;height:150px;border-radius:50%;background:var(--paper);border:2.5px solid var(--sky);display:flex;align-items:center;justify-content:center;text-align:center}
  .badge-name{font-family:"Oswald",sans-serif;font-size:12.5px;color:#222;line-height:1.2}
  .contact{position:absolute;left:300px;top:574px;width:290px;text-align:center;color:var(--paper);font-weight:700;font-size:12px;line-height:15.5px}
  .tagline{position:absolute;left:600px;top:605px;width:296px;text-align:center;color:var(--paper);font-size:12px}
</style>
</head>
<body>
<div class="flyer">
  <div class="top-band"></div>

  <div class="photo photo-lips" role="img" aria-label="Foto: Unterspritzung an den Lippen, behandschuhte Hände mit Spritze"></div>
  <div class="photo photo-eye" role="img" aria-label="Foto: Injektion an der Schläfe neben dem Auge"></div>
  <div class="photo photo-face" role="img" aria-label="Foto: Frauenporträt mit Lippenunterspritzung"></div>

  <h2 class="section-title title-lumex">Lumex</h2>
  <div class="copy copy-lumex">
    <p>Botulinumtoxin wird in der Medizin zur Therapie<br>von Muskelspasmen eingesetzt und vermindert<br>die Muskeltätigkeit.</p>
    <p>Im ästhetischen Bereich eignet sich dieses<br>Produkt zur Faltentherapie, v.a. im Stirn- und<br>Glabellabereich sowie bei „Krähenfüßen“. Mittels<br>kleiner und so gut wie schmerzfreier Injektionen<br>werden geringe Mengen in definierte Punkte ein-<br>gebracht, nach 2-6 Tagen setzt die Wirkung<br>ein und hält für 10-12 Monate an.</p>
    <p>Nach mehrmaligen Behandlungen verlängert<br>sich die Wirkdauer.</p>
  </div>

  <h2 class="section-title title-prp">PRP-Therapie</h2>
  <div class="copy copy-prp">
    <p>Bei der „Eigenblutbehandlung“<br>(engl. „platelet rich plasma“, PRP) wird<br>mittels spezieller Zentrifugation aus Eigen-Blut ein<br>Plättchen-angereichertes Plasma mit einer Vielzahl<br>von Wachstumsfaktoren gewonnen. Dieses wird<br>dann mittels kleinster Kanülen sub- bzw. intrakutan<br>injiziert. Typische Anwendungsbereiche sind Stimu-<br>lation des Haarwachstums im Kopfbereich, Faltenbe-<br>handlung („Perlglanzkur“), Narben, Schwangerschafts-<br>streifen und Couperose („prominente Äderchen“).</p>
    <p>Der große Vorteil der Behandlung liegt in der Thera-<br>pie mit körpereigenen Stoffen ohne Fremdmaterial.<br>Eine Kombination mit einer „Needling-Therapie“ ist<br>in vielen Fällen sinnvoll.</p>
    <p>Für ein ästhetisches Ergebnis sind meist<br>2-3 Sitzungen notwendig.</p>
  </div>

  <svg class="wave" width="900" height="636" viewBox="0 0 900 636" aria-hidden="true">
    <defs>
      <linearGradient id="waveFill" x1="0" y1="0" x2="1" y2="0">
        <stop offset="0" stop-color="#7cc4e6"/>
        <stop offset="0.55" stop-color="#4a7f9c"/>
        <stop offset="1" stop-color="#2a4d63"/>
      </linearGradient>
    </defs>
    <path d="M0,585 C250,575 480,560 640,530 C760,507 840,482 900,445 L900,636 L0,636 Z" fill="url(#waveFill)"/>
  </svg>

  <div class="badge"><span class="badge-name">Dr. med. Stefan Duriklem</span></div>

  <div class="contact">Kontakt:<br>Dr. Stefan Duriklem<br>Lindenauer Str. 48 &nbsp;| 06120 Musterstadt</div>
  <div class="tagline">Ihr Arzt für Ästhetisch-kosmetische Medizin.</div>
</div>
</body>
</html>
```